Carpet cleaning company wants business card

Need an exciting new fresh design for business cards for my carpet cleaning /pest control business
www.tidewellhomecare.com.au
Can design include a lined section for quoting or information? Thanks !

```html
<!DOCTYPE html>
<html lang="en">
<head>
<meta charset="utf-8">
<title>Tidewell Home Care – Business Card</title>
<link href="https://fonts.googleapis.com/css2?family=Arimo:wght@400;700&display=swap" rel="stylesheet">
<style>
  :root {
    --brand-blue: #0f5aa8;
    --brand-red: #e8383a;
    --paper: #ffffff;
    --ink: #1d3f73;
    --ink-soft: #4a4a4a;
    --rule-light: rgba(255,255,255,0.55);
    --backdrop: #e9ebee;
  }
  * { margin: 0; padding: 0; box-sizing: border-box; }
  html, body { width: 1200px; height: 900px; overflow: hidden; }
  body {
    background: var(--backdrop);
    font-family: "Arimo", Arial, sans-serif;
    position: relative;
  }
  .card {
    position: absolute;
    width: 700px;
    height: 400px;
    border-radius: 18px;
    overflow: hidden;
    box-shadow: 0 10px 30px rgba(0,0,0,0.18);
  }
  .brand {
    position: absolute;
    display: flex; align-items: center; gap: 16px;
    white-space: nowrap;
  }
  .brand-mark { background: var(--brand-red); flex: none; }
  .brand-name { font-weight: 700; line-height: 1; letter-spacing: 1px; }

  /* Front */
  .card-front {
    left: 110px; top: 40px;
    background: var(--brand-blue);
    color: var(--paper);
  }
  .card-front .brand { left: 0; right: 0; top: 110px; justify-content: center; }
  .card-front .brand-mark { width: 24px; height: 24px; }
  .card-front .brand-name { color: var(--paper); font-size: 48px; }
  .card-front .web {
    position: absolute;
    left: 0; right: 0; top: 205px;
    text-align: center;
    font-size: 19px;
    letter-spacing: 2px;
  }
  .web .domain { color: var(--brand-red); }
  .quote-lines {
    position: absolute;
    left: 120px; right: 120px; top: 270px;
    list-style: none;
  }
  .quote-lines li {
    height: 32px;
    border-bottom: 1px solid var(--rule-light);
  }

  /* Back */
  .card-back {
    left: 390px; top: 470px;
    background: var(--paper);
  }
  .card-back .brand { left: 200px; top: 46px; gap: 12px; }
  .card-back .brand-mark { width: 18px; height: 18px; }
  .card-back .brand-name { color: var(--brand-blue); font-size: 34px; }

  .person {
    position: absolute;
    left: 40px; top: 168px;
    width: 280px;
    text-align: right;
    white-space: nowrap;
  }
  .person-name { font-weight: 700; font-size: 26px; letter-spacing: 0.5px; }
  .person-name .first { color: var(--brand-red); }
  .person-name .last { color: var(--brand-blue); }
  .person-role { font-size: 18px; color: var(--ink-soft); margin-top: 4px; }

  .divider {
    position: absolute;
    left: 345px; top: 130px;
    width: 1.5px; height: 115px;
    background: var(--brand-red);
  }
  .contacts {
    position: absolute;
    left: 368px; top: 128px;
    list-style: none;
    font-size: 16px;
    color: var(--ink);
    white-space: nowrap;
  }
  .contacts li { display: flex; align-items: center; gap: 8px; height: 29px; }
  .contacts svg { width: 14px; height: 14px; fill: var(--brand-blue); flex: none; }

  .address-band {
    position: absolute;
    left: 0; right: 0; top: 285px;
    height: 66px;
    background: var(--brand-blue);
    color: var(--paper);
    display: flex; align-items: center; justify-content: center;
    font-size: 20px;
    letter-spacing: 0.5px;
  }
</style>
</head>
<body>

  <section class="card card-front" aria-label="Business card front">
    <div class="brand">
      <span class="brand-mark"></span>
      <span class="brand-name">TIDEWELL HOME CARE</span>
    </div>
    <p class="web">www.<span class="domain">tidewellhomecare</span>.com.au</p>
    <ul class="quote-lines" aria-label="Lined section for quotes and notes">
      <li></li><li></li><li></li>
    </ul>
  </section>

  <section class="card card-back" aria-label="Business card back">
    <div class="brand">
      <span class="brand-mark"></span>
      <span class="brand-name">TIDEWELL HOME CARE</span>
    </div>

    <div class="person">
      <p class="person-name"><span class="first">MAREN</span> <span class="last">HOLLOWAY</span></p>
      <p class="person-role">Owner/CEO</p>
    </div>

    <div class="divider"></div>

    <ul class="contacts">
      <li>
        <svg viewBox="0 0 16 16" aria-hidden="true"><path d="M3.5 1.5l2.5 2.6-1.3 1.8a9 9 0 0 0 5.4 5.4l1.8-1.3 2.6 2.5-1.6 2A12.5 12.5 0 0 1 1.5 3.1z"/></svg>
        07 5120 4486
      </li>
      <li>
        <svg viewBox="0 0 16 16" aria-hidden="true"><path d="M4.5 1h7a1 1 0 0 1 1 1v12a1 1 0 0 1-1 1h-7a1 1 0 0 1-1-1V2a1 1 0 0 1 1-1zm.5 2v9h6V3zm3 10a.7.7 0 1 0 0 1.4.7.7 0 0 0 0-1.4z"/></svg>
        0412 730 259
      </li>
      <li>
        <svg viewBox="0 0 16 16" aria-hidden="true"><path d="M1 3h14v10H1zm1.5 1.2v.4L8 8.6l5.5-4v-.4zM2.5 6.3v5.5h11V6.3L8 10.2z"/></svg>
        admin@tidewellhomecare.com.au
      </li>
      <li>
        <svg viewBox="0 0 16 16" aria-hidden="true"><path d="M8 1a7 7 0 1 0 0 14A7 7 0 0 0 8 1zm0 1.5c.8 0 1.8 1.6 2.1 4H5.9C6.2 4.1 7.2 2.5 8 2.5zM2.6 7.5h2.1a12 12 0 0 0 0 1H2.6zm8.7 0h2.1v1h-2.1a12 12 0 0 0 0-1zM5.9 9.5h4.2c-.3 2.4-1.3 4-2.1 4s-1.8-1.6-2.1-4z"/></svg>
        www.tidewellhomecare.com.au
      </li>
    </ul>

    <div class="address-band">1270 Harbourline Rd Coral Vale, 40218</div>
  </section>

</body>
</html>
```